A corporate website

The target design is for Vellmar Glassworks coporate site which is a major international manufacturers for the finest quality of transparent and colored full lead crystal (more than 30% PbO)

Vellmar Glassworks is the largest producer of crystal in world with 98% of its production exported to more than 120 countries.

Vellmar Glassworks has 4 business lines:
1. Crystal Fashion Components
2. Chandeliers Crystal Parts
3. Lighting Collection and special design
4. Gifts and accessories

The winner bidder(s) would be asked to do more jobs

The corporate website is the official site that represents Vellmar HQ in front of world and it includes the following pages:
1. Home page
2. Facilities:
a. Factories overview
b. Factories image and video gallery
c. Show rooms locator
d. Quality Control
3. Media Center with the following sub pages
a. Press releases (Previous and future press releases)
b. Logos & artwork (Hi res images for Vellmar Glassworks to be used by various worldwide media)
c. Media contacts (contacts of Vellmar’s media division)
4. Careers:
a. Publish opened positions from Pindle hire
b. Capture candidates resumes using Pindle hire form
5. About US

Target Market(s)

Business partners, resellers, end customers, press and employees

Industry/Entity Type

Business

Requirements
Must have
• The design should include a home webpage and an internal page design. The design should fullfill the following requriements:

1. Strictly follow the corporate identity materials guidelines - see attachment
2. Supports multi-language
3. User can change between languages using flags
4. Web surfer can optionally change the default language
5. An integrated live chat push button for ChatBrio
8. Site Header should contain the following information:
a. Logo
b. Slogan
c. Links to site pages
d. Link to the home page
e. Link to the landing page
f. A language option drop box
9. Footers should have:
a. Links to all other 5 websites in a dropbox form
b. Link to privacy statement
c. Link to copyright notice
d. Link to sitemap
e. Newsletter subscription one field form
11. Every sub-site should have a universal customer service section that offer the following services:
a. Links to end user installation manuals
b. Links to products cleaning and maintenance guide
c. Customer complaints center
12. A news sub-section that should contain:
a. Latest product and promotional announcements
b. Corporate news
c. Exhibitions coverage
13. A link to vellmar Worldwide:
a. A database driven interactive map reflecting Vellmar list of agents and distributors worldwide with list of supported products this interactive map could be limited in every sub-site for specific line of product
b. Capture potential resellers and agents
c. Become a partner form

```html
<!DOCTYPE html>
<html lang="en">
<head>
<meta charset="utf-8">
<title>Vellmar Glassworks</title>
<link rel="stylesheet" href="https://fonts.googleapis.com/css2?family=Arimo:wght@400;700&family=Archivo+Black&display=swap">
<style>
:root{
  --bg:#000;
  --ink:#fff;
  --nav:#d8d8d8;
  --muted:#8a8a8a;
  --dim:#5e5e5e;
  --teal:#006f72;
  --slide-grey:#2b2b2b;
  --submit:#6f9a3d;
  --card:#fff;
  --brand-ink:#222;
}
*{box-sizing:border-box;margin:0;padding:0}
a{text-decoration:none;color:inherit}
html,body{width:1200px;height:922px;overflow:hidden;background:var(--bg)}
body{position:relative;font-family:"Arimo",Arial,sans-serif;color:var(--ink)}
.halo{position:absolute;left:300px;top:-120px;width:600px;height:420px;
  background:radial-gradient(ellipse at 50% 30%,rgba(183,162,28,.85) 0%,rgba(80,110,40,.55) 22%,rgba(20,70,70,.35) 45%,rgba(0,0,0,0) 70%)}
.horizon{position:absolute;left:120px;width:960px;height:24px;
  background:radial-gradient(ellipse at 50% 50%,rgba(60,200,210,.7) 0%,rgba(30,143,154,.35) 30%,rgba(0,0,0,0) 70%)}
.horizon.top{top:180px}
.horizon.bottom{top:795px;opacity:.6}
.logo-card{position:absolute;left:493px;top:47px;width:215px;height:153px;background:var(--card);
  border-radius:20px 20px 0 0;display:flex;flex-direction:column;align-items:center;justify-content:center;gap:10px}
.logo-card .dot{width:48px;height:48px;border-radius:50%;background:#8f8f8f}
.logo-card .brand{font-size:17px;letter-spacing:3px;color:var(--brand-ink);font-weight:400;text-transform:uppercase;text-align:center;line-height:1.2}
.live-support{position:absolute;left:846px;top:31px;width:124px;height:38px;background:linear-gradient(#c7c7c7,#8d8d8d);
  display:flex;align-items:center;gap:6px;padding-left:6px;font-size:13px;font-weight:700;color:#fff}
.live-support .lamp{width:26px;height:26px;border-radius:50%;background:radial-gradient(circle,#9be86a 30%,#3d9a20 70%);border:2px solid #fff}
.live-support small{display:block;font-size:9px;letter-spacing:2px;font-style:italic}
.lang{position:absolute;left:982px;top:31px;width:101px;height:20px;border:1px solid #777;display:flex;align-items:center;font-size:12px;color:var(--muted)}
.lang .flag{width:14px;height:9px;background:#8aa0c8;margin:0 10px 0 8px}
.lang .arrow,.site-select .arrow{margin-left:auto;width:16px;height:18px;background:#fff;position:relative}
.arrow::after{content:"";position:absolute;left:4px;top:7px;border:4px solid transparent;border-top:5px solid #000}
.main-nav{position:absolute;top:251px;left:0;width:1200px;display:flex;justify-content:center;gap:40px;padding-left:4px}
.main-nav a{color:var(--nav);font-weight:700;font-size:13px}
.slider{position:absolute;left:183px;top:308px;width:832px;height:268px}
.slide-figure{position:absolute;left:0;top:0;width:460px;height:268px;background:linear-gradient(90deg,var(--slide-grey),#262626 80%,rgba(0,0,0,0))}
.slide-photo{position:absolute;left:460px;top:-30px;width:372px;height:298px;
  background:radial-gradient(ellipse at 55% 45%,#d9dde0 0%,#7aa8bb 22%,#1f7f8c 45%,rgba(120,130,40,.4) 60%,rgba(0,0,0,0) 75%)}
.slide-copy{position:absolute;left:38px;top:80px;width:450px}
.slide-copy h1{font-family:"Archivo Black",Arial,sans-serif;font-weight:400;font-size:33px;line-height:44px;color:#ececec;letter-spacing:-.3px}
.slide-copy h1 .small{font-size:17px}
.slide-copy p{margin-top:20px;width:440px;font-size:12px;line-height:18px;color:#c9c9c9}
.slider-btn{position:absolute;top:427px;width:37px;height:37px;border-radius:50%;background:radial-gradient(circle at 40% 35%,#fafafa,#bdbdbd 75%);
  box-shadow:0 0 0 1px #6a6a6a;display:flex;align-items:center;justify-content:center}
.slider-btn.prev{left:122px}.slider-btn.next{left:1044px}
.service{position:absolute;top:670px;width:229px;height:108px;background:var(--teal);color:#fff;font-weight:700;font-size:16px;line-height:20px;text-align:right}
.service .label{position:absolute;right:20px;top:26px}
.service .icon{position:absolute;left:14px;top:14px;width:110px;height:82px;border-radius:6px}
.service.manuals{left:120px}.service.manuals .icon{background:linear-gradient(#f4f4f4,#c9c2b3)}
.service.complaints{left:363px}.service.complaints .icon{left:22px;width:90px;background:linear-gradient(#e9eef5,#9fb4d8)}
.service.cleaning{left:607px}.service.cleaning .label{top:22px}.service.cleaning .icon{width:70px;opacity:.85;background:linear-gradient(#f4a23c,#d97a16)}
.newsletter{position:absolute;left:853px;top:670px;width:229px;height:108px;background:var(--teal);padding:15px 19px 0}
.newsletter h2{font-weight:400;font-size:16px;color:#fff}
.newsletter .field{margin-top:6px;width:191px;height:23px;background:#fff;border:1px solid #bbb;font-size:11px;color:#999;padding:4px 7px}
.newsletter .submit{margin:7px 0 0 108px;width:82px;height:25px;background:linear-gradient(#8ab452,var(--submit));font-weight:700;font-size:12px;color:#fff;display:flex;align-items:center;justify-content:center}
.site-select{position:absolute;left:122px;top:836px;width:165px;height:21px;border:1px solid #777;display:flex;align-items:center;padding-left:6px;font-size:13px;color:var(--dim)}
.footer-links{position:absolute;right:119px;top:839px;text-align:right;font-size:12px;color:var(--dim);line-height:19px;letter-spacing:.6px}
.footer-links a{color:var(--dim)}
.footer-links .copy{font-size:10px;letter-spacing:.6px}
</style>
</head>
<body>
<div class="halo"></div>
<div class="horizon top"></div>

<header>
  <a class="logo-card" href="#">
    <span class="dot"></span>
    <span class="brand">Vellmar<br>Glassworks</span>
  </a>
  <a class="live-support" href="#"><span class="lamp"></span><span>Live Support<small>ONLINE</small></span></a>
  <div class="lang"><span class="flag"></span>English<span class="arrow"></span></div>
  <nav class="main-nav">
    <a href="#">Home</a><a href="#">Facilities</a><a href="#">Media Center</a><a href="#">Careers</a><a href="#">About Us</a>
  </nav>
</header>

<section class="slider">
  <div class="slide-figure" role="img" aria-label="Grey silhouette of a figure holding up a crystal"></div>
  <div class="slide-photo" role="img" aria-label="Photograph of two cut crystal diamonds glowing in teal light"></div>
  <div class="slide-copy">
    <h1>LIGHTING COLLECTION<br><span class="small">AND </span>SPECIAL DESIGN</h1>
    <p>Vellmar Glassworks is the largest international manufacturers for the finest quality of transparent and colored full lead crystal. 98% of its production exported to more than 120 countries.</p>
  </div>
</section>
<a class="slider-btn prev" href="#" aria-label="Previous"><svg width="12" height="14" viewBox="0 0 12 14"><path d="M9 1 3 7l6 6" fill="none" stroke="#333" stroke-width="3"/></svg></a>
<a class="slider-btn next" href="#" aria-label="Next"><svg width="12" height="14" viewBox="0 0 12 14"><path d="M3 1l6 6-6 6" fill="none" stroke="#333" stroke-width="3"/></svg></a>

<section class="customer-service">
  <a class="service manuals" href="#"><span class="icon" role="img" aria-label="Open book illustration"></span><span class="label">End User<br>Installation<br>Manuals</span></a>
  <a class="service complaints" href="#"><span class="icon" role="img" aria-label="Form window with pencil illustration"></span><span class="label">Customer<br>Complaints<br>Center</span></a>
  <a class="service cleaning" href="#"><span class="icon" role="img" aria-label="Life ring illustration"></span><span class="label">Products<br>Cleaning and<br>Maintenance Guide</span></a>
  <form class="newsletter">
    <h2>Newsletter Subscription</h2>
    <div class="field">Email ID</div>
    <div class="submit">SUBMIT</div>
  </form>
</section>

<div class="horizon bottom"></div>

<footer>
  <div class="site-select">Lorem Ipsum is simply<span class="arrow"></span></div>
  <div class="footer-links">
    <a href="#">Become a Partner</a> | <a href="#">Privacy Statement</a> | <a href="#">Sitemap</a><br>
    <span class="copy">Copyright2011 VellmarGlassworks All rights reserved</span>
  </div>
</footer>
</body>
</html>
```